Landscape Contractor in need of New Web Design

HELP.. Please Help!!!!. Our current website is old, outdated, ugly... and well nothing like us.... so we are looking for someone to help build a new website that fits our company direction. We are a landscape company with multiple locations in order to meet the needs of our clients and their projects throughout the midwest. When most people think of landscaping, they think of mowing grandmas yard, but that is NOT even remotely close to what we do. We are 100% a commercial landscape company meaning we complete landscape and irrigation services for large scale commercial projects. We are looking for a website to showcase our commercial talents and awesome team of people.
Updates

Address of current website is www.brookvaleyardworks.com

```html
<!DOCTYPE html>
<html lang="en">
<head>
<meta charset="utf-8">
<title>Brookvale Yardworks – Landscape Maintenance Service</title>
<link href="https://fonts.googleapis.com/css2?family=Oswald:wght@400;500;600&family=Roboto+Slab:wght@400;500&family=PT+Serif:wght@400&display=swap" rel="stylesheet">
<style>
:root{
  --lime:#b2f000;
  --ink:#151515;
  --text:#333333;
  --muted:#555555;
  --paper:#ffffff;
  --mist:#f2f2f2;
  --night:#1d1d1b;
  --footer-text:#e6e6e6;
}
*{margin:0;padding:0;box-sizing:border-box}
html,body{width:1200px;height:4882px;overflow:hidden}
body{position:relative;background:var(--paper);color:var(--text);font-family:"PT Serif",serif}
.abs{position:absolute}
.head{font-family:"Oswald",sans-serif;font-weight:600;text-transform:uppercase;color:var(--ink)}
.section-title{position:absolute;left:0;width:1200px;text-align:center;font-family:"Oswald",sans-serif;font-weight:600;font-size:38px;color:var(--ink);text-transform:uppercase;letter-spacing:.3px}
.btn{position:absolute;background:var(--lime);color:var(--ink);font-family:"Oswald",sans-serif;font-weight:500;font-size:14px;text-transform:uppercase;display:flex;align-items:center;justify-content:center;text-decoration:none}

.topbar{left:0;top:0;width:1200px;height:32px;background:var(--ink);color:#fff;font-size:12px}
.topbar .hours{left:121px;top:0;height:32px;display:flex;align-items:center;gap:8px}
.topbar .phones{left:745px;top:0;height:32px;display:flex;align-items:center;gap:8px}
.topbar .pay{left:973px;top:6px;width:105px;height:20px;background:#fff;color:var(--ink);font-family:"Oswald",sans-serif;font-size:10px;font-weight:500;display:flex;align-items:center;justify-content:center}

.header{left:0;top:32px;width:1200px;height:80px;background:var(--paper)}
.brand{left:121px;top:20px;display:flex;align-items:center;gap:8px}
.brand-dot{width:40px;height:40px;border-radius:50%;background:var(--lime)}
.brand-name{font-family:"Oswald",sans-serif;font-weight:600;font-size:17px;color:var(--ink)}
.nav{left:513px;top:0;height:80px;display:flex;align-items:center;gap:27px;font-family:"Oswald",sans-serif;font-size:13px;color:var(--ink)}
.nav .active{color:#8cc400;border-bottom:1px solid #8cc400}
.quote{left:953px;top:21px;width:125px;height:39px;font-size:15px}

.hero-photo{left:0;top:112px;width:1200px;height:525px;background:linear-gradient(180deg,#8e98a0 0%,#7b8587 18%,#6b6a55 30%,#3f5a23 45%,#2f4a19 70%,#213713 100%)}
.hero-strip{left:0;top:637px;width:121px;height:61px;background:#213713}
.hero-rule{left:121px;top:400px;width:4px;height:190px;background:var(--lime)}
.hero-title{left:150px;top:392px;font-family:"Oswald",sans-serif;font-weight:600;font-size:50px;color:#fff;text-transform:uppercase;letter-spacing:.2px}
.hero-copy{left:150px;top:462px;width:680px;font-size:14.5px;line-height:22px;color:#fff}
.hero-cta{left:150px;top:533px;width:144px;height:40px}

.service{position:absolute;width:247px;height:264px;border-left:4px solid var(--lime);background:var(--paper)}
.service .photo{width:100%;height:184px}
.service .label{position:absolute;left:17px;top:184px;height:80px;display:flex;align-items:center;font-family:"Roboto Slab",serif;font-size:18px;color:var(--ink);line-height:21px}

.why{left:0;top:1486px;width:1200px;height:347px;background:var(--mist)}
.feature{position:absolute;top:1619px;width:144px;height:152px;display:flex;flex-direction:column;align-items:center;font-size:12.5px;color:var(--ink)}
.feature.is-active{background:var(--lime)}
.feature .badge{margin-top:24px;width:66px;height:66px;border-radius:50%;background:#e6e6e6;display:flex;align-items:center;justify-content:center}
.feature.is-active .badge{background:#fff;border:2px solid var(--ink)}
.feature .badge-inner{width:48px;height:48px;border-radius:50%;background:#fff;display:flex;align-items:center;justify-content:center}
.feature .name{margin-top:14px}

.who-photo{left:121px;top:1896px;width:389px;height:381px;border-radius:0 70px 0 70px;background:linear-gradient(180deg,#b9c9d3 0%,#9fb0a8 35%,#5b8f36 62%,#d86a5a 80%,#4f8a2c 100%)}
.who-title{left:609px;top:1942px;font-size:38px}
.who-copy{left:609px;top:2003px;width:470px;font-size:12.4px;line-height:21.8px;color:var(--text)}
.who-cta{left:609px;top:2180px;width:131px;height:40px}

.gallery-band{left:0;top:2340px;width:1200px;height:300px;background:linear-gradient(180deg,#8d8d8d 0%,#6e6e6e 45%,#3a3a3a 100%)}
.gallery-title{color:#fff;top:2386px}
.shot{position:absolute;top:2470px;height:344px;border-radius:8px}
.arrow{position:absolute;width:46px;height:46px;border-radius:50%;display:flex;align-items:center;justify-content:center}
.arrow.light{background:#fff}
.arrow.dark{background:var(--ink)}

.reviews{left:0;top:2967px;width:1200px;height:598px;background:var(--mist)}
.review{position:absolute;top:3100px;width:307px;height:311px;background:var(--paper);border-radius:6px;text-align:center}
.review .avatar{width:74px;height:74px;border-radius:50%;margin:26px auto 0;background:linear-gradient(180deg,#c9c9c9,#8d8d8d)}
.review .stars{margin-top:26px;display:flex;justify-content:center;gap:2px}
.review .quote-text{margin:16px auto 0;width:250px;font-size:12.4px;line-height:22px;color:var(--text)}
.review .who{margin-top:14px;font-family:"Oswald",sans-serif;font-size:14px;color:var(--ink);text-transform:uppercase}

.post{position:absolute;top:3697px;width:387px}
.post .photo{width:387px;height:319px}
.post .date{margin-top:30px;font-family:"Oswald",sans-serif;font-size:11.5px;color:var(--ink);text-transform:uppercase}
.post .title{margin-top:18px;font-family:"Oswald",sans-serif;font-weight:500;font-size:21px;line-height:29px;color:var(--ink);text-transform:uppercase}
.post .excerpt{margin-top:12px;font-size:12.6px;line-height:21.5px;color:var(--text);width:372px}
.post .more{margin-top:12px;font-family:"Oswald",sans-serif;font-size:12px;color:var(--ink);text-decoration:underline}

.footer{left:0;top:4414px;width:1200px;height:468px;background:radial-gradient(ellipse at 50% 30%,#3b3a33 0%,#26251f 45%,#161613 100%)}
.foot-h{position:absolute;font-family:"Oswald",sans-serif;font-weight:500;font-size:14px;color:#fff;text-transform:uppercase}
.foot-t{position:absolute;font-size:11px;line-height:21px;color:var(--footer-text)}
.newsletter{left:121px;top:4511px;width:243px;height:34px;border:2px solid #fff;display:flex;align-items:center;justify-content:space-between;padding-left:8px}
.newsletter span{font-size:10.5px;color:#fff}
.newsletter .go{width:60px;height:26px;background:var(--lime);display:flex;align-items:center;justify-content:center;margin-right:2px}
.social{left:965px;top:4527px;display:flex;gap:14px}
.social i{display:block;width:14px;height:14px;border-radius:50%;background:#fff}
.foot-rule{left:121px;top:4835px;width:957px;height:1px;background:#6d6d6d}
.legal{top:4850px;font-size:10px;color:var(--footer-text)}
</style>
</head>
<body>

<div class="abs topbar">
  <div class="abs hours">
    <svg width="16" height="16" viewBox="0 0 16 16"><circle cx="8" cy="8" r="6.5" fill="none" stroke="#fff" stroke-width="1.4"/><path d="M8 4.5V8l2.5 1.5" fill="none" stroke="#fff" stroke-width="1.4"/></svg>
    <span>Business Hours: 8am - 5pm : Mon - Fri</span>
  </div>
  <div class="abs phones">
    <svg width="16" height="16" viewBox="0 0 16 16"><path d="M3 2.5l2.5-.5 1.5 3-1.5 1.2a8 8 0 0 0 4 4L10.8 8.7l3 1.5-.5 2.5C9 13 3.5 8 3 2.5z" fill="none" stroke="#fff" stroke-width="1.3"/></svg>
    <span>(555) 318-2047 / (555) 604-7713</span>
  </div>
  <div class="abs pay">MAKE A PAYMENT</div>
</div>

<header class="abs header">
  <div class="abs brand"><span class="brand-dot"></span><span class="brand-name">Brookvale Yardworks</span></div>
  <nav class="abs nav">
    <span class="active">HOME</span><span>DIVISIONS</span><span>SERVICES</span><span>ABOUT US</span><span>GALLERY</span><span>CONTACT</span>
  </nav>
  <a class="btn quote">GET A QUOTE</a>
</header>

<div class="abs hero-photo" role="img" aria-label="Irrigated crop field with sprinklers running toward distant hills under a cloudy sky"></div>
<div class="abs hero-strip"></div>
<div class="abs hero-rule"></div>
<h1 class="abs hero-title">Landscape Maintenance Service</h1>
<p class="abs hero-copy">We are a landscape company with multiple locations in order to meet the needs of our clients and their projects throughout the midwest.</p>
<a class="btn hero-cta">GET STARTED</a>

<h2 class="section-title" style="top:688px">Our Services</h2>

<div class="service" style="left:228px;top:766px">
  <div class="photo" role="img" aria-label="Lawn sprinkler watering a curved garden path with shrubs" style="background:linear-gradient(180deg,#7fae45,#5c9a2a 55%,#9a8a6c)"></div>
  <div class="label">Maintenance&nbsp;
    <svg width="16" height="14" viewBox="0 0 16 14"><path d="M2 2l5 5-5 5M8 2l5 5-5 5" fill="none" stroke="#151515" stroke-width="2"/></svg>
  </div>
</div>
<div class="service" style="left:476px;top:766px">
  <div class="photo" role="img" aria-label="Gardener scooping fertilizer from a bowl over young plants" style="background:linear-gradient(180deg,#3f5f8a,#5a7d3a 60%,#4f3f2a)"></div>
  <div class="label">Chemical Applications<br>&amp; Fertilization</div>
</div>
<div class="service" style="left:724px;top:766px">
  <div class="photo" role="img" aria-label="Gloved hands planting seedlings in soil" style="background:linear-gradient(180deg,#4b6d32,#3f5a2b 50%,#5a4a3a)"></div>
  <div class="label">Turf Management</div>
</div>
<div class="service" style="left:228px;top:1067px">
  <div class="photo" role="img" aria-label="Stone block retaining wall with paved patio and hedges" style="background:linear-gradient(180deg,#5c8a2e,#9c9a96 40%,#8a8884)"></div>
  <div class="label">Hardscaping</div>
</div>
<div class="service" style="left:476px;top:1067px">
  <div class="photo" role="img" aria-label="Sprinklers spraying a lawn lined with palm trees" style="background:linear-gradient(180deg,#c9d3d8,#7b9a5a 45%,#3f7a22)"></div>
  <div class="label">Irrigation</div>
</div>
<div class="service" style="left:724px;top:1067px">
  <div class="photo" role="img" aria-label="Worker laying sod rolls beside a paver path" style="background:linear-gradient(180deg,#9a9892,#7d8a6a 50%,#4e7a2a)"></div>
  <div class="label">Landscaping</div>
</div>

<a class="btn" style="left:521px;top:1382px;width:156px;height:40px">VIEW ALL SERVICES</a>

<div class="abs why"></div>
<h2 class="section-title" style="top:1539px">Why Choose Us</h2>

<div class="feature" style="left:121px">
  <div class="badge"><div class="badge-inner"><svg width="24" height="24" viewBox="0 0 24 24"><path d="M5 19C5 10 11 5 20 4c0 9-5 15-13 15M5 19l8-8" fill="none" stroke="#333" stroke-width="1.5"/></svg></div></div>
  <div class="name">Specialized Company</div>
</div>
<div class="feature is-active" style="left:284px">
  <div class="badge"><div class="badge-inner"><svg width="26" height="26" viewBox="0 0 26 26"><path d="M13 5a6 6 0 0 0-3.5 10.8V18h7v-2.2A6 6 0 0 0 13 5zM10 20.5h6M11 23h4M13 1v2M4 4l1.5 1.5M22 4l-1.5 1.5M1 12h2M23 12h2" fill="none" stroke="#151515" stroke-width="1.5"/></svg></div></div>
  <div class="name">Licensed &amp; Insured</div>
</div>
<div class="feature" style="left:447px">
  <div class="badge"><div class="badge-inner"><svg width="26" height="26" viewBox="0 0 26 26"><rect x="3" y="8" width="11" height="8" fill="none" stroke="#333" stroke-width="1.5"/><path d="M14 11h5l3 4v1h-8" fill="none" stroke="#333" stroke-width="1.5"/><circle cx="7" cy="19" r="3" fill="none" stroke="#333" stroke-width="1.5"/><circle cx="19" cy="19" r="2" fill="none" stroke="#333" stroke-width="1.5"/></svg></div></div>
  <div class="name">Dependable Services</div>
</div>
<div class="feature" style="left:609px">
  <div class="badge"><div class="badge-inner"><svg width="24" height="24" viewBox="0 0 24 24"><rect x="3" y="5" width="18" height="16" fill="none" stroke="#333" stroke-width="1.5"/><path d="M3 9h18M8 3v4M16 3v4M8 15l3 3 5-5" fill="none" stroke="#333" stroke-width="1.5"/></svg></div></div>
  <div class="name">Day Scheduling</div>
</div>
<div class="feature" style="left:772px">
  <div class="badge"><div class="badge-inner"><svg width="26" height="26" viewBox="0 0 26 26"><circle cx="13" cy="13" r="10" fill="none" stroke="#333" stroke-width="1.5"/><circle cx="13" cy="11" r="3" fill="none" stroke="#333" stroke-width="1.5"/><path d="M8 18a5 5 0 0 1 10 0" fill="none" stroke="#333" stroke-width="1.5"/></svg></div></div>
  <div class="name">Free Consultations</div>
</div>
<div class="feature" style="left:935px">
  <div class="badge"><div class="badge-inner"><svg width="26" height="26" viewBox="0 0 26 26"><circle cx="13" cy="7" r="3" fill="none" stroke="#333" stroke-width="1.5"/><circle cx="6" cy="11" r="2.5" fill="none" stroke="#333" stroke-width="1.5"/><circle cx="20" cy="11" r="2.5" fill="none" stroke="#333" stroke-width="1.5"/><path d="M8 22v-5a5 5 0 0 1 10 0v5M2 22v-3a4 4 0 0 1 5-4M24 22v-3a4 4 0 0 0-5-4" fill="none" stroke="#333" stroke-width="1.5"/></svg></div></div>
  <div class="name">Reputable Company</div>
</div>

<div class="abs who-photo" role="img" aria-label="Landscaper in safety helmet trimming grass beside flower beds in a city park"></div>
<h2 class="abs head who-title">Who We Are</h2>
<p class="abs who-copy">Founded by Owen Harlow and Miles Tanner, Brookvale Yardworks is the premier landscape maintenance and design company based in Fairbrook, Kansas. Our company's dedication to innovative design projects created some of the most distinguished landscape projects throughout Kansas, Missouri, and Oklahoma. eiusmod tempor incididunt ut labore et dolore magna aliqua. Quis ipsum suspendisse ultrices gravida. Risus commodo viverra maecenas accumsan lacus vel facilisis.</p>
<a class="btn who-cta">MEET OUR TEAM</a>

<div class="abs gallery-band" role="img" aria-label="Dark farm field at dusk"></div>
<h2 class="section-title gallery-title">Our Gallery</h2>
<div class="shot" style="left:0;width:104px;border-radius:0 8px 8px 0;background:linear-gradient(180deg,#8aa4c0,#c9a94a 55%,#b08a2e)" role="img" aria-label="Combine harvester in a golden wheat field"></div>
<div class="shot" style="left:121px;width:226px;background:linear-gradient(160deg,#4f8a2e,#6ba83a 50%,#3e6e24)" role="img" aria-label="Aerial view of a worker mowing a lawn beside a curved path"></div>
<div class="shot" style="left:366px;width:226px;background:linear-gradient(180deg,#3f6e2a,#5e8e3a 55%,#6a5a3a)" role="img" aria-label="Farmer harvesting vegetables between green crop rows"></div>
<div class="shot" style="left:609px;width:225px;background:linear-gradient(180deg,#d96aa8,#e9d7e0 35%,#a8957a 60%,#5f9a32)" role="img" aria-label="Curved stone edging around a bed of pink and white flowers"></div>
<div class="shot" style="left:853px;width:226px;background:linear-gradient(180deg,#8fb3d6,#7e9a5a 45%,#4a3a2a)" role="img" aria-label="Red tractor working a ploughed field"></div>
<div class="shot" style="left:1096px;width:104px;border-radius:8px 0 0 8px;background:linear-gradient(180deg,#6a8f4a,#b8a58a 55%,#5f9a32)" role="img" aria-label="Stone retaining wall with planted terrace"></div>
<div class="arrow light" style="left:142px;top:2618px"><svg width="14" height="14" viewBox="0 0 14 14"><path d="M9 2L4 7l5 5" fill="none" stroke="#151515" stroke-width="2.2"/></svg></div>
<div class="arrow light" style="left:1012px;top:2618px"><svg width="14" height="14" viewBox="0 0 14 14"><path d="M5 2l5 5-5 5" fill="none" stroke="#151515" stroke-width="2.2"/></svg></div>
<a class="btn" style="left:518px;top:2867px;width:163px;height:38px">VIEW ALL GALLERIES</a>

<div class="abs reviews"></div>
<h2 class="section-title" style="top:3022px">Customer Reviews</h2>

<div class="review" style="left:121px">
  <div class="avatar" role="img" aria-label="Customer portrait"></div>
  <div class="stars"><svg width="92" height="16" viewBox="0 0 92 16"><g fill="#f5b800"><path id="st" d="M8 1l2.1 4.6 5 .5-3.8 3.3 1.1 5L8 11.8 3.6 14.4l1.1-5L.9 6.1l5-.5z"/><use href="#st" x="19"/><use href="#st" x="38"/><use href="#st" x="57"/><use href="#st" x="76"/></g></svg></div>
  <p class="quote-text">Have been using the liquid form and discovered the gummies as much easier for traveling. No refrigeration needed and so easy to ta...</p>
  <div class="who">- Marla T.</div>
</div>
<div class="review" style="left:446px">
  <div class="avatar" role="img" aria-label="Customer portrait" style="background:linear-gradient(180deg,#f2c9a8,#d8936a)"></div>
  <div class="stars"><svg width="92" height="16" viewBox="0 0 92 16"><g fill="#f5b800"><use href="#st"/><use href="#st" x="19"/><use href="#st" x="38"/><use href="#st" x="57"/><use href="#st" x="76"/></g></svg></div>
  <p class="quote-text">Have been using the liquid form and discovered the gummies as much easier for traveling. No refrigeration needed and so easy to ta...</p>
  <div class="who">- Marla T.</div>
</div>
<div class="review" style="left:772px">
  <div class="avatar" role="img" aria-label="Customer portrait"></div>
  <div class="stars"><svg width="92" height="16" viewBox="0 0 92 16"><g fill="#f5b800"><use href="#st"/><use href="#st" x="19"/><use href="#st" x="38"/><use href="#st" x="57"/><use href="#st" x="76"/></g></svg></div>
  <p class="quote-text">Have been using the liquid form and discovered the gummies as much easier for traveling. No refrigeration needed and so easy to ta...</p>
  <div class="who">- Marla T.</div>
</div>
<div class="arrow dark" style="left:57px;top:3232px"><svg width="14" height="14" viewBox="0 0 14 14"><path d="M9 2L4 7l5 5" fill="none" stroke="#fff" stroke-width="2.2"/></svg></div>
<div class="arrow dark" style="left:1095px;top:3232px"><svg width="14" height="14" viewBox="0 0 14 14"><path d="M5 2l5 5-5 5" fill="none" stroke="#fff" stroke-width="2.2"/></svg></div>
<a class="btn" style="left:518px;top:3462px;width:163px;height:40px">VIEW ALL REVIEWS</a>

<h2 class="section-title" style="top:3619px">Our Blogs</h2>
<article class="post" style="left:203px">
  <div class="photo" role="img" aria-label="Combine harvester cutting a wheat field under blue sky" style="background:linear-gradient(180deg,#3f77c0,#a8c4e0 40%,#c9a24a 60%,#a37e34)"></div>
  <div class="date">Published 07/24/2021</div>
  <h3 class="title">U.S and Russia: Phosphate Import Dutiesagricultural Groups Speak...</h3>
  <p class="excerpt">In a letter sent to the Regional Trade Review Board on February 17, 2021, the Prairie Grain Growers Guild, the Heartland Seed Producers Alliance, and the Plains Fiber Council joined...</p>
  <div class="more">READ MORE</div>
</article>
<article class="post" style="left:609px">
  <div class="photo" role="img" aria-label="Landscaper placing flagstones in a garden bed" style="background:linear-gradient(180deg,#3f6e2a,#5e8a3a 40%,#9a9488 70%,#6f6a60)"></div>
  <div class="date">Published 07/24/2021</div>
  <h3 class="title">U.S and Russia: Phosphate Import Dutiesagricultural Groups Speak...</h3>
  <p class="excerpt">In a letter sent to the Regional Trade Review Board on February 17, 2021, the Prairie Grain Growers Guild, the Heartland Seed Producers Alliance, and the Plains Fiber Council joined...</p>
  <div class="more">READ MORE</div>
</article>
<div class="arrow dark" style="left:142px;top:3833px"><svg width="14" height="14" viewBox="0 0 14 14"><path d="M9 2L4 7l5 5" fill="none" stroke="#fff" stroke-width="2.2"/></svg></div>
<div class="arrow dark" style="left:1012px;top:3833px"><svg width="14" height="14" viewBox="0 0 14 14"><path d="M5 2l5 5-5 5" fill="none" stroke="#fff" stroke-width="2.2"/></svg></div>
<a class="btn" style="left:518px;top:4310px;width:163px;height:40px">READ ALL BLOGS</a>

<footer class="abs footer" role="img" aria-label="Tractor in a field at dusk behind the footer"></footer>
<div class="foot-h" style="left:121px;top:4476px">Sign - Up For Our Newsletter</div>
<div class="abs newsletter"><span>Enter Email</span><div class="go"><svg width="22" height="12" viewBox="0 0 22 12"><path d="M1 6h18M14 1l5 5-5 5" fill="none" stroke="#151515" stroke-width="1.8"/></svg></div></div>
<div class="foot-h" style="left:965px;top:4476px">Follow Us On</div>
<div class="abs social"><i></i><i></i><i></i></div>

<div class="foot-h" style="left:121px;top:4594px">About Us</div>
<p class="foot-t" style="left:121px;top:4628px;width:230px">Brookvale Yardworks strives to set the standard for the highest quality lawn and landscape products and services and to exceed our customer's expectations every time.</p>

<div class="foot-h" style="left:487px;top:4594px">Our Services</div>
<p class="foot-t" style="left:487px;top:4628px;line-height:24px">Turf Management<br>Hardscaping<br>Irrigation<br>Landscaping</p>

<div class="foot-h" style="left:732px;top:4594px">Quick Links</div>
<p class="foot-t" style="left:732px;top:4628px;line-height:24px">About Us<br>Divisions<br>Certifications<br>Gallery</p>

<div class="foot-h" style="left:965px;top:4594px">Contact Us</div>
<p class="foot-t" style="left:965px;top:4628px;line-height:17px">Addres:<br>Brookvale Yardworks Inc.<br>4180 Meadowline Court<br>Fairbrook, KS 66990<br>Westmere Office:<br>1-555-318-2047<br>Cedar Bend Office:<br>1-555-604-7713</p>

<div class="abs foot-rule"></div>
<div class="abs legal" style="left:121px">Copyright 2021 Brookvale Yardworks Inc. All Rights Reserved.</div>
<div class="abs legal" style="left:927px">Privacy Policy &nbsp; | &nbsp; Terms of use</div>

</body>
</html>
```